Luxury Brand Coffee Table Book Template

Overview:
We are creating a premium, 28-page coffee table book to accompany every bespoke jewelry piece handcrafted by Marrowind Jewelry. This book serves as an heirloom that documents the story, design, and craftsmanship behind each custom piece, culminating in a powerful legacy statement. We need a refined, luxurious, and masculine layout template that can be updated for each new customer.
**All reference files (images, logos, copy for pages, etc.) are included in the .zip file.
Deliverables:
Print-ready 28-page InDesign or editable template file
Front and back cover design
Consistent typography and page layouts based on our outlined structure
Design system that allows for easy photo and text updates per client
Specs:
Size: 8.1 x 10.6 in, Portrait Orientation
Cover: Black linen hardcover with gold foil stamped name or crest (simulated in mockup)
Interior: Deep matte photo paper feel – minimalistic, clean layout with generous whitespace
Color Palette: Black, white, and gold
Style: Bold, masculine, timeless, high-luxury (think Veltrane Studio x Brisselle & Co.)
See the attached 28-page outline. Please use stock image placeholders for now.
Target Market(s)
Affluent Men & Women age 35-65
Industry/Entity Type
Luxury Retail Jewelry
Font styles to use
Other font styles liked:
- I really like Trajan Pro 3, but open to suggestions, as well as a mixture of Serif and Sans Serif fonts
Look and feel
Each slider illustrates characteristics of the customer's brand and the style your logo design should communicate.

```html
<!DOCTYPE html>
<html lang="en">
<head>
<meta charset="utf-8">
<title>Marrowind Jewelry – Book Pages</title>
<link rel="stylesheet" href="https://fonts.googleapis.com/css2?family=Montserrat:wght@400;800&display=swap">
<style>
  :root {
    --backdrop: #9b9b9b;
    --page-black: #000000;
    --ink-white: #ffffff;
    --gold-deep: #c8952b;
    --gold-mid: #deb24a;
    --gold-light: #f8eaa8;
    --gold-text: #d9ad45;
  }
  * { margin: 0; padding: 0; box-sizing: border-box; }
  html, body {
    width: 862px;
    height: 1200px;
    overflow: hidden;
    background: var(--backdrop);
  }
  .canvas {
    position: relative;
    width: 862px;
    height: 1200px;
    background: var(--backdrop);
    font-family: "Montserrat", sans-serif;
  }
  .page {
    position: absolute;
    background: var(--page-black);
    overflow: hidden;
    box-shadow: 4px 6px 10px rgba(0, 0, 0, 0.28);
  }
  .page--cover { left: 229px; top: 56px; width: 405px; height: 529px; }
  .page--photo { left: 63px; top: 661px; width: 352px; height: 459px; }
  .page--story { left: 446px; top: 661px; width: 352px; height: 459px; }

  .cover-shapes { position: absolute; inset: 0; width: 100%; height: 100%; }

  .cover-title {
    position: absolute;
    left: 57px;
    top: 259px;
    color: var(--ink-white);
    font-weight: 800;
    font-size: 31px;
    line-height: 41px;
    letter-spacing: 0.2px;
    text-transform: uppercase;
  }

  .photo-placeholder {
    position: absolute;
    inset: 0;
    background:
      radial-gradient(ellipse 30% 26% at 48% 52%, rgba(225, 228, 240, 0.85), rgba(225, 228, 240, 0) 100%),
      radial-gradient(ellipse 70% 22% at 45% 40%, rgba(176, 140, 80, 0.55), rgba(176, 140, 80, 0) 100%),
      radial-gradient(ellipse 60% 14% at 60% 10%, rgba(150, 120, 70, 0.35), rgba(150, 120, 70, 0) 100%),
      linear-gradient(180deg, #0a0805 0%, #050403 60%, #0b0a0d 100%);
  }

  .story-pattern {
    position: absolute;
    left: 0;
    top: 0;
    width: 100%;
    height: 150px;
    background: linear-gradient(180deg, rgba(201, 150, 43, 0.28) 0%, rgba(201, 150, 43, 0.08) 70%, rgba(0, 0, 0, 0) 100%);
  }

  .story-heading {
    position: absolute;
    left: 0;
    width: 100%;
    top: 224px;
    text-align: center;
    font-weight: 400;
    font-size: 63px;
    line-height: 63px;
    letter-spacing: 1px;
    background: linear-gradient(100deg, var(--gold-deep) 0%, var(--gold-light) 45%, var(--gold-mid) 70%, var(--gold-deep) 100%);
    -webkit-background-clip: text;
    background-clip: text;
    color: transparent;
  }

  .story-body {
    position: absolute;
    left: 33px;
    width: 286px;
    top: 315px;
    color: var(--ink-white);
    font-weight: 400;
    font-size: 7.6px;
    line-height: 10.1px;
    text-align: center;
  }
</style>
</head>
<body>
  <main class="canvas">

    <section class="page page--cover">
      <svg class="cover-shapes" viewBox="0 0 405 529" aria-hidden="true">
        <defs>
          <linearGradient id="gold-foil" x1="0" y1="0" x2="1" y2="1">
            <stop offset="0" stop-color="#d7a93c"/>
            <stop offset="0.38" stop-color="#f8eaa8"/>
            <stop offset="0.7" stop-color="#e3b954"/>
            <stop offset="1" stop-color="#c8952b"/>
          </linearGradient>
        </defs>
        <polygon class="cover-chevron" points="0,0 405,0 202,202" fill="url(#gold-foil)"/>
        <polygon class="cover-band" points="405,310 405,443 314,529 184,529" fill="url(#gold-foil)"/>
      </svg>
      <h1 class="cover-title">Marrowind<br>Jewelry</h1>
    </section>

    <section class="page page--photo">
      <div class="photo-placeholder" role="img" aria-label="Close-up photograph of a gold ring set with a large round diamond on a black background"></div>
    </section>

    <section class="page page--story">
      <div class="story-pattern" role="img" aria-label="Fine gold line pattern of angular facets across the top of the page"></div>
      <h2 class="story-heading">STORY</h2>
      <p class="story-body">Every piece begins with a conversation about the moments that matter most to you. Our goldsmiths listen, sketch and refine until the design carries your story in metal and stone. Each diamond is chosen by hand for its fire, clarity and balance, then set with patience in our workshop. Weeks of careful shaping, polishing and fitting turn a first idea into an heirloom made to last. This book records that journey, from the first drawing to the final setting, so that the story travels with the jewel. May it be opened for generations, and may every reader feel the care, the craft and the devotion within these pages.</p>
    </section>

  </main>
</body>
</html>
```